Recruitment of Brindle Staffing for the UK market

I want a website for the UK market to attract businesses and companies to come to us for Philipine labour. We want an information site that gives all information on what we do and how we can recruit Philippine labour.
This is a recruitment site for companies to contact us with their requirements for skilled workers coming from the Philipines over to the UK to work.

Target Market(s)

Uk Companies and businesses who want Philipine skilled workers

Industry/Entity Type

REcruitment

Coding

Coded - Design and coding required

Number of Pages Required

5+ page

Font styles to use
Sans Serif

Colors
0054AA
0677BA
7BADD7
CADEEF
E8F1F8
0094D4
00A9DD
6FCCEA
C7EBF8
E9F6FB
EE7325
F08F49
F5BC92
FAE3D3
FDF4ED
EB3D1F
EC4F4E
F09395
F8D3D4
FCEDEE

Requirements
Must have
• Look professional and corperate with drop down menus for Home ,about, services,articles. training , contact us
Nice to have
• Look at Tovel recruitment- https://tovelrecruitment.example.co.uk/. This is my current site - https://www.brindlestaffing.example.com/
Should not have
• Cartoons or silly pictures , needs to be corperate looking

```html
<!DOCTYPE html>
<html lang="en">
<head>
<meta charset="utf-8">
<title>Brindle Staffing – Skilled Philippine Workers for UK Companies</title>
<link rel="stylesheet" href="https://fonts.googleapis.com/css2?family=Roboto:wght@400;500;700&display=swap">
<style>
:root{
  --red:#EB3D1F;
  --red-soft:#EC4F4E;
  --ink:#111111;
  --text:#5a5a5a;
  --muted:#6b6b6b;
  --line:#ececec;
  --white:#ffffff;
  --logo:#9a2a22;
}
*{margin:0;padding:0;box-sizing:border-box}
html,body{width:1200px;height:3603px;overflow:hidden;background:var(--white)}
body{position:relative;font-family:'Roboto',sans-serif;color:var(--ink)}
.abs{position:absolute}
.top-rule{left:0;top:0;width:1200px;height:4px;background:var(--red)}
.brand{font-weight:700;color:var(--logo);font-size:26px;letter-spacing:.5px;display:flex;align-items:center;gap:10px}
.brand-mark{width:22px;height:22px;background:var(--logo)}
.header-brand{left:112px;top:40px}
.btn{background:var(--red);color:var(--white);font-weight:500;font-size:15px;display:flex;align-items:center;justify-content:center;border-radius:2px}
.quote-btn{left:965px;top:23px;width:122px;height:40px}
.main-nav{top:78px;left:570px;font-size:15px;font-weight:500}
.main-nav span{position:absolute;white-space:nowrap}
.hero{left:0;top:122px;width:1200px;height:622px;background:linear-gradient(180deg,#c9c3bb 0%,#8e8780 45%,#5d5a57 75%,#4b4a48 100%)}
.hero-title{left:0;top:540px;width:1200px;text-align:center;color:var(--white);font-size:40px;font-weight:500;line-height:52px;text-transform:uppercase}
.hero-btn{left:540px;top:660px;width:121px;height:40px}
.section-title{font-size:30px;font-weight:500;text-transform:uppercase;line-height:41px}
.skills-title{left:110px;top:848px;width:340px}
.skills-text{left:112px;top:942px;width:330px;font-size:15.5px;line-height:29px;color:var(--text)}
.viewall-btn{left:112px;top:1134px;width:122px;height:41px}
.skill-grid{left:506px;top:834px;width:572px;height:360px;display:grid;grid-template-columns:repeat(3,1fr);grid-template-rows:repeat(2,1fr);box-shadow:0 2px 14px rgba(0,0,0,.08)}
.skill{display:flex;flex-direction:column;align-items:center;justify-content:flex-end;padding-bottom:30px;font-size:15px;font-weight:500;color:#333;background:var(--white)}
.skill.is-accent{background:linear-gradient(180deg,var(--red-soft),var(--red));color:var(--white)}
.skill-icon{width:62px;height:70px;margin-bottom:22px;border:2.5px solid currentColor;border-radius:8px;opacity:.9}
.skill:not(.is-accent) .skill-icon{border-color:var(--red)}
.about-title{left:0;top:1311px;width:1200px;text-align:center}
.about-text{left:171px;top:1367px;width:860px;text-align:center;font-size:15.5px;line-height:26px;color:var(--text)}
.card{top:1488px;width:302px;height:372px;border-radius:42px 0 42px 0;background:var(--white);box-shadow:0 3px 16px rgba(0,0,0,.09);text-align:center;padding:40px 34px 0}
.card.is-accent{background:linear-gradient(180deg,var(--red-soft),var(--red));color:var(--white)}
.card-icon{width:86px;height:86px;margin:0 auto;border-radius:50%;background:var(--red);display:flex;align-items:center;justify-content:center}
.card.is-accent .card-icon{background:var(--white)}
.card h3{font-size:19px;font-weight:500;margin-top:22px}
.card p{font-size:12.5px;line-height:22.5px;color:var(--muted);margin-top:13px}
.card.is-accent p{color:var(--white)}
.band{left:0;top:1986px;width:1200px;height:498px;background:linear-gradient(110deg,#7a5a4a 0%,#3d3a38 35%,#5a5753 70%,#48453f 100%)}
.band-circle{left:111px;top:2014px;width:442px;height:442px;border-radius:50%;background:var(--white);box-shadow:0 0 0 0 transparent,inset 0 0 0 20px #f2f2f2;display:flex;align-items:center;justify-content:center;text-align:center;font-size:35px;font-weight:500;line-height:50px;padding:0 70px}
.map{left:123px;top:2576px;width:463px;height:453px;border-radius:3px;background:linear-gradient(160deg,#8fb0f5,#9db9f3)}
.contact-title{left:638px;top:2615px}
.contact-text{left:638px;top:2670px;width:455px;font-size:15.5px;line-height:27.5px;color:var(--text)}
.contact-item{left:638px;display:flex;align-items:flex-start;gap:14px;font-size:15.5px;color:var(--text);line-height:27px}
.contact-icon{width:26px;height:26px;border-radius:50%;background:var(--red);flex:none;display:flex;align-items:center;justify-content:center}
.footer-brand{left:0;top:3172px;width:1200px;justify-content:center}
.footer-nav{top:3255px;left:0;width:1200px;display:flex;justify-content:center;gap:38px;font-size:15px;font-weight:500}
.socials{top:3297px;left:0;width:1200px;display:flex;justify-content:center;gap:12px}
.socials span{width:23px;height:23px;border-radius:50%;background:var(--red)}
.copyright{top:3337px;left:0;width:1200px;text-align:center;font-size:14.5px;font-weight:500;color:#333}
.skyline{left:0;top:3400px;width:1200px;height:203px;background:linear-gradient(180deg,#ffffff 0%,#dfe6ee 45%,#aab6c4 100%)}
</style>
</head>
<body>
<div class="abs top-rule"></div>

<header>
  <div class="abs brand header-brand"><span class="brand-mark"></span>Brindle Staffing</div>
  <a class="abs btn quote-btn">Get A Quote</a>
  <nav class="abs main-nav">
    <span style="left:0">Home</span>
    <span style="left:80px">About</span>
    <span style="left:160px">Services</span>
    <span style="left:257px">Articles</span>
    <span style="left:349px">Training</span>
    <span style="left:443px">Contact us</span>
  </nav>
</header>

<section>
  <div class="abs hero" role="img" aria-label="Photo of job candidates seated in a row of chairs waiting for interviews"></div>
  <h1 class="abs hero-title">Recruiting and placing skilled Philippine<br>workers into UK companies</h1>
  <a class="abs btn hero-btn">Get Started</a>
</section>

<section>
  <h2 class="abs section-title skills-title">UK Skilled Workers List</h2>
  <p class="abs skills-text">The UK government since brexit have developed a new system based on points (similar to Australia) when recruiting from outside of the UK. Previuosly EU citizens could work in the UK without any extensive documentation or clarification of skills. This has all changed.</p>
  <a class="abs btn viewall-btn">View All</a>
  <div class="abs skill-grid">
    <div class="skill is-accent"><span class="skill-icon" role="img" aria-label="Civil engineer icon"></span>Civil engineer</div>
    <div class="skill"><span class="skill-icon" role="img" aria-label="Restaurant manager icon"></span>Restaurant manager</div>
    <div class="skill is-accent"><span class="skill-icon" role="img" aria-label="Technical director icon"></span>Technical director</div>
    <div class="skill"><span class="skill-icon" role="img" aria-label="Café owner icon"></span>Café owner</div>
    <div class="skill is-accent"><span class="skill-icon" role="img" aria-label="Electrical engineer icon"></span>Electrical engineer</div>
    <div class="skill"><span class="skill-icon" role="img" aria-label="Internet developer icon"></span>Internet developer</div>
  </div>
</section>

<section>
  <h2 class="abs section-title about-title">What the business is about</h2>
  <p class="abs about-text">We source skilled workers directly from the Philippines to work in the UK. With offices , training locations and specialist recruiters we can find the highest quality individuals to add value and resources to any UK buisness. We delivery quality based on vast experience over a number of years.</p>

  <article class="abs card" style="left:110px">
    <div class="card-icon"><svg width="40" height="40" viewBox="0 0 40 40" fill="none" stroke="#fff" stroke-width="2.5"><circle cx="20" cy="14" r="7"/><path d="M7 35c2-8 7-11 13-11s11 3 13 11"/></svg></div>
    <h3>What we do</h3>
    <p>Our company has been estabilished in the Philippines for over 20 years. We have mainly been recruiting philippine workers for the off shore industry in asia but since brexit and the new rules on skilled workers entering the UK we have been working with UK companies</p>
  </article>
  <article class="abs card is-accent" style="left:449px">
    <div class="card-icon"><svg width="40" height="40" viewBox="0 0 40 40" fill="none" stroke="#EB3D1F" stroke-width="2.5"><path d="M7 9h26v17H17l-7 6v-6H7z"/><path d="M14 18h1M20 18h1M26 18h1"/></svg></div>
    <h3>How we help</h3>
    <p>We work with companies to find skilled workers that meet the UK requirements for Visas and work permits. We guide you through the whole process and deliver highly trained people that add value to your business.</p>
  </article>
  <article class="abs card" style="left:787px">
    <div class="card-icon"><svg width="44" height="44" viewBox="0 0 44 44" fill="none" stroke="#fff" stroke-width="2.5"><circle cx="22" cy="22" r="17"/><path d="M16.5 17a5.5 5.5 0 1 1 7.5 5c-1.3.6-2 1.6-2 3v2"/><circle cx="22" cy="32" r="1" fill="#fff"/></svg></div>
    <h3>Where to start</h3>
    <p>We need to know what your issues are and how we can understand the personnal you require , over what time frame and the number of employees you need. Once this is estabilished we start sourcing workers in the Philippines that meet your criteria</p>
  </article>
</section>

<section>
  <div class="abs band" role="img" aria-label="Photo of a magnet attracting colourful wooden people figures"></div>
  <div class="abs band-circle">We recruit the finest talent available with our dedicated 200 strong team.</div>
</section>

<section>
  <div class="abs map" role="img" aria-label="Map of the Philippines"></div>
  <h2 class="abs section-title contact-title">Contact us today</h2>
  <p class="abs contact-text">Please contact us today with your requirements , this can be care workers ,chef, welders, pipe fitters, caravan cabinet makers, medical workers. The UK list of required skills is extensive and the Philippines offersenglish speaking highly qualified hard working employees. Contact us today and make that first step to a highly motivated , quality skilled workforce.</p>
  <div class="abs contact-item" style="top:2858px"><span class="contact-icon"><svg width="14" height="14" viewBox="0 0 24 24" fill="#fff"><path d="M6.6 10.8a15 15 0 0 0 6.6 6.6l2.2-2.2c.3-.3.7-.4 1-.2 1.1.4 2.3.6 3.6.6.6 0 1 .4 1 1V20c0 .6-.4 1-1 1A17 17 0 0 1 3 4c0-.6.4-1 1-1h3.5c.6 0 1 .4 1 1 0 1.3.2 2.5.6 3.6.1.3 0 .7-.2 1z"/></svg></span>07700 900123</div>
  <div class="abs contact-item" style="top:2895px"><span class="contact-icon"><svg width="14" height="14" viewBox="0 0 24 24" fill="none" stroke="#fff" stroke-width="2.4"><rect x="3" y="5" width="18" height="14" rx="1"/><path d="M3 6l9 7 9-7"/></svg></span>sales@brindlestaffing.example.com</div>
  <div class="abs contact-item" style="top:2932px"><span class="contact-icon"><svg width="14" height="14" viewBox="0 0 24 24" fill="#fff"><path d="M12 2a7 7 0 0 0-7 7c0 5 7 13 7 13s7-8 7-13a7 7 0 0 0-7-7zm0 9.5a2.5 2.5 0 1 1 0-5 2.5 2.5 0 0 1 0 5z"/></svg></span><span>12 Maple Court, Eastbridge EB1 4QT<br>United Kingdom</span></div>
</section>

<footer>
  <div class="abs brand footer-brand"><span class="brand-mark"></span>Brindle Staffing</div>
  <nav class="abs footer-nav"><span>Home</span><span>About</span><span>Services</span><span>Articles</span><span>Training</span><span>Contact us</span></nav>
  <div class="abs socials"><span></span><span></span><span></span><span></span></div>
  <p class="abs copyright">© 2023 All Rights Reserved | Brindle Staffing Ltd</p>
  <div class="abs skyline" role="img" aria-label="Faded photo of a city skyline"></div>
</footer>
</body>
</html>
```